Emergency Management Consulting Flyer

Company name: Stone Harbor Emergency Management

I am looking for a postcard design for my emergency management consulting business. I'm looking for something that has some colors and is double sided, on side with the information on services provided and the other side with the contact information. For the main side I'm looking for the following:

How prepared are you?

Services Provided:
Healthcare Preparedness
EOC Support
Emergency Planning
Mitigation Planning
Business Continuity
Disaster Response
Training and Exercises
Project Management
And more

Affordable for small and large organizations
Stand-by contracts available

On the back side, I'm looking for Contact Us section.

Overall I'm looking for something a bit more modern and need to have at least one disaster photo. If you have questions please message me.

Target Market(s)

Government, Healthcare Facilities, Businesses

Industry/Entity Type

Consulting

Requirements
Must have
• Disaster Picture, modern looking
• For the main side I'm looking for the following:
• How prepared are you?
• Services Provided:
• Healthcare Preparedness
• EOC Support
• Emergency Planning
• Mitigation Planning
• Business Continuity
• Disaster Response
• Training and Exercises
• Project Management
• And more
• Affordable for small and large organizations
• Stand-by contracts available

```html
<!DOCTYPE html>
<html lang="en">
<head>
<meta charset="utf-8">
<title>Stone Harbor Emergency Management – Postcard</title>
<link rel="stylesheet" href="https://fonts.googleapis.com/css2?family=Montserrat:wght@800;900&family=Open+Sans:wght@400;600;700&display=swap">
<style>
  :root {
    --red: #e0312a;
    --yellow: #f7c70f;
    --blue: #1763a6;
    --navy: #1f3f8f;
    --ink: #222428;
    --grey-text: #4a4d52;
    --paper: #ffffff;
    --paper-shade: #ececec;
    --backdrop: #e9eaec;
  }
  * { box-sizing: border-box; margin: 0; padding: 0; }
  html, body { width: 1200px; height: 1076px; overflow: hidden; }
  body { background: var(--backdrop); font-family: "Open Sans", sans-serif; position: relative; }

  .postcard {
    position: absolute; width: 600px; height: 456px; overflow: hidden;
    background: linear-gradient(135deg, var(--paper-shade), var(--paper) 60%);
    box-shadow: 0 10px 30px rgba(0,0,0,.25);
  }
  .postcard--front { left: 110px; top: 70px; }
  .postcard--back { left: 490px; top: 560px; background: var(--paper); }
  .postcard__shapes { position: absolute; inset: 0; width: 100%; height: 100%; }
  .postcard > *:not(.postcard__shapes) { position: absolute; }

  .headline {
    left: 30px; top: 44px; color: var(--paper); white-space: nowrap;
    font-family: "Montserrat", sans-serif; font-weight: 900; font-size: 34px; letter-spacing: .5px;
    transform: rotate(-4deg); transform-origin: left center;
  }
  .services-title { left: 40px; top: 138px; color: var(--red); font-weight: 700; font-size: 18px; }
  .service-list { list-style: none; }
  .service-list--left { left: 40px; top: 168px; }
  .service-list--right { left: 290px; top: 136px; }
  .service-list li {
    display: flex; align-items: center; gap: 10px; height: 34px;
    font-size: 16px; color: var(--ink); white-space: nowrap;
  }
  .service-icon {
    width: 22px; height: 22px; border-radius: 50%; background: var(--red);
    border: 2px solid #f4b8b5; flex: none; position: relative;
  }
  .service-icon::after {
    content: ""; position: absolute; inset: 5px; border-radius: 50%; border: 2px solid var(--paper);
  }
  .benefits { left: 44px; top: 310px; list-style: none; }
  .benefits li {
    display: flex; align-items: center; gap: 10px; height: 25px;
    color: var(--navy); font-weight: 600; font-size: 13px; white-space: nowrap;
  }
  .tick { width: 16px; height: 16px; flex: none; }

  .brand { display: flex; align-items: center; gap: 10px; }
  .brand__dot { width: 28px; height: 28px; border-radius: 50%; background: var(--red); flex: none; }
  .brand__name { font-weight: 700; font-size: 13px; color: var(--grey-text); white-space: nowrap; }
  .postcard--front .brand { left: 40px; top: 364px; }
  .postcard--back .brand { left: 40px; top: 336px; }

  .photo-circle {
    width: 108px; height: 108px; border-radius: 50%;
    border: 3px solid var(--red); box-shadow: 0 0 0 3px var(--paper);
  }
  .photo-circle--fire { left: 364px; top: 300px; background: radial-gradient(circle at 40% 55%, #f59a2b, #b4431a 45%, #2a1a12 85%); }
  .photo-circle--flood { left: 484px; top: 284px; background: linear-gradient(180deg, #dfe7ec 0%, #c8d4da 35%, #8a7a68 62%, #6b6a52 100%); }

  .website { color: var(--paper); font-size: 11px; white-space: nowrap; }
  .postcard--front .website { right: 30px; top: 424px; transform: rotate(-4deg); }
  .postcard--back .website { left: 36px; top: 420px; transform: rotate(-3deg); }

  .disaster-photo { right: 0; top: 0; width: 430px; height: 400px;
    background: linear-gradient(90deg, rgba(255,255,255,1) 0%, rgba(220,220,220,.6) 30%, #a9a9a9 60%, #7c7c7c 100%); }
  .contact-title {
    left: 20px; top: 40px; color: var(--paper); white-space: nowrap;
    font-family: "Montserrat", sans-serif; font-weight: 800; font-size: 30px;
    transform: rotate(-3deg); transform-origin: left center;
  }
  .contact-intro { left: 30px; top: 150px; color: var(--blue); font-weight: 700; font-size: 15px; line-height: 1.45; }
  .contact-list { left: 30px; top: 208px; list-style: none; color: var(--ink); }
  .contact-list li { display: flex; align-items: flex-start; gap: 8px; }
  .contact-list .contact-phone { font-size: 30px; font-weight: 600; align-items: center; }
  .contact-list .contact-line { font-size: 14px; margin-top: 4px; line-height: 1.45; }
  .contact-icon { width: 14px; height: 14px; flex: none; margin-top: 3px; }
  .contact-phone .contact-icon { width: 20px; height: 20px; margin-top: 0; }
</style>
</head>
<body>

<section class="postcard postcard--front" aria-label="Front: services">
  <svg class="postcard__shapes" viewBox="0 0 600 456" preserveAspectRatio="none" aria-hidden="true">
    <path d="M0 0H600V44C520 114 400 146 280 144C170 142 80 128 0 134Z" fill="var(--blue)"/>
    <path d="M0 0H600V32C520 102 400 134 280 132C170 130 80 116 0 122Z" fill="var(--yellow)"/>
    <path d="M0 0H600V20C520 90 400 122 280 120C170 118 80 104 0 110Z" fill="var(--red)"/>
    <path d="M0 456V392C110 448 260 450 600 372V456Z" fill="var(--red)"/>
    <path d="M0 456V400C110 456 260 458 600 380V456Z" fill="var(--yellow)"/>
    <path d="M0 456V410C110 466 260 466 600 390V456Z" fill="var(--blue)"/>
  </svg>

  <h1 class="headline">HOW PREPARED ARE YOU?</h1>
  <h2 class="services-title">Services Provided:</h2>
  <ul class="service-list service-list--left">
    <li><span class="service-icon"></span>Healthcare Preparedness</li>
    <li><span class="service-icon"></span>EOC Support</li>
    <li><span class="service-icon"></span>Emergency Planning</li>
    <li><span class="service-icon"></span>Mitigation Planning</li>
  </ul>
  <ul class="service-list service-list--right">
    <li><span class="service-icon"></span>Business Continuity</li>
    <li><span class="service-icon"></span>Disaster Response</li>
    <li><span class="service-icon"></span>Training and Exercises</li>
    <li><span class="service-icon"></span>Project Management And more</li>
  </ul>
  <ul class="benefits">
    <li><svg class="tick" viewBox="0 0 16 16"><rect x="1" y="4" width="11" height="11" fill="none" stroke="var(--red)" stroke-width="1.6"/><path d="M3.5 9l3 3L15 2" fill="none" stroke="var(--red)" stroke-width="2"/></svg>Affordable for small &amp; large organizations</li>
    <li><svg class="tick" viewBox="0 0 16 16"><rect x="1" y="4" width="11" height="11" fill="none" stroke="var(--red)" stroke-width="1.6"/><path d="M3.5 9l3 3L15 2" fill="none" stroke="var(--red)" stroke-width="2"/></svg>Stand-by contracts available</li>
  </ul>

  <div class="brand"><span class="brand__dot"></span><span class="brand__name">Stone Harbor Emergency Management</span></div>

  <div class="photo-circle photo-circle--fire" role="img" aria-label="Photo of firefighters spraying water at a large blaze"></div>
  <div class="photo-circle photo-circle--flood" role="img" aria-label="Photo of a flooded house"></div>

  <p class="website">www.StoneHarborEmergencyManagement.com</p>
</section>

<section class="postcard postcard--back" aria-label="Back: contact details">
  <div class="disaster-photo" role="img" aria-label="Black and white photo of a person standing before a house destroyed by a storm"></div>
  <svg class="postcard__shapes" viewBox="0 0 600 456" preserveAspectRatio="none" aria-hidden="true">
    <path d="M0 0H370C310 70 200 100 0 118Z" fill="var(--blue)"/>
    <path d="M0 0H362C302 64 196 92 0 110Z" fill="var(--paper)"/>
    <path d="M0 0H352C292 58 190 84 0 100Z" fill="var(--red)"/>
    <path d="M0 456V400C140 350 330 360 600 392V456Z" fill="var(--red)"/>
    <path d="M0 456V408C140 360 330 368 600 400V456Z" fill="var(--yellow)"/>
    <path d="M0 456V418C140 370 330 378 600 410V456Z" fill="var(--blue)"/>
  </svg>

  <h2 class="contact-title">Contact Details</h2>
  <p class="contact-intro">For more information,<br>Contact us anyday, any time</p>
  <ul class="contact-list">
    <li class="contact-phone"><svg class="contact-icon" viewBox="0 0 20 20"><path d="M5 2l3 4-2 2c1 3 3 5 6 6l2-2 4 3-2 3C9 18 2 11 2 4Z" fill="var(--red)"/></svg>123-456-7890</li>
    <li class="contact-line"><svg class="contact-icon" viewBox="0 0 14 14"><rect x="1" y="3" width="12" height="8" fill="var(--red)"/><path d="M1 3l6 5 6-5" fill="none" stroke="#fff" stroke-width="1.2"/></svg>Info@companyname.com</li>
    <li class="contact-line"><svg class="contact-icon" viewBox="0 0 14 14"><path d="M7 1a4 4 0 0 1 4 4c0 3-4 8-4 8S3 8 3 5a4 4 0 0 1 4-4Z" fill="var(--red)"/><circle cx="7" cy="5" r="1.5" fill="#fff"/></svg>Address of the company<br>countryname</li>
  </ul>

  <div class="brand"><span class="brand__dot"></span><span class="brand__name">Stone Harbor Emergency Management</span></div>

  <p class="website">www.StoneHarborEmergencyManagement.com</p>
</section>

</body>
</html>
```